Chatterbox and Pictoria advertisment

We need Chatterbox and Pictoria ads.  Simple ad with Alaska themed background.
This ad is to introduce our new KORVO Internet service.
--Speeds to 500 mbps
-- Packages start at only $89.99 for speeds to 100mbps
-- Fiber Optic based connection, Not satellite
-- Extreme low latency, consistent speeds
--FREE equipment, FREE Installation, FREE wifi router, First month of service FREE

This is for a Chatterbox/Pictoria ad. We already have a logo

```html
<!DOCTYPE html>
<html lang="en">
<head>
<meta charset="utf-8">
<title>KORVO Internet – Chatterbox &amp; Pictoria</title>
<link rel="stylesheet" href="https://fonts.googleapis.com/css2?family=Roboto:wght@400;500;700&family=Barlow+Condensed:wght@500;600;700&family=Barlow+Semi+Condensed:wght@500;600&display=swap">
<style>
  :root {
    --navy: #061428;
    --night: #0b1d3a;
    --aurora-teal: #1fc6d8;
    --aurora-blue: #3f7fe0;
    --aurora-violet: #5a4fd0;
    --brand-blue: #0b4a9e;
    --brand-blue-dark: #083a80;
    --accent-red: #e8213a;
    --white: #ffffff;
    --ink: #111111;
    --muted-ink: #2a2a2a;
  }
  * { margin: 0; padding: 0; box-sizing: border-box; }
  html, body { width: 1200px; height: 1200px; overflow: hidden; background: var(--navy); }
  .ad {
    position: relative; width: 1200px; height: 1200px; overflow: hidden;
    font-family: "Roboto", Arial, sans-serif; color: var(--white);
    background: var(--navy);
  }
  .scene {
    position: absolute; inset: 0;
    background:
      radial-gradient(ellipse 520px 260px at 950px 300px, rgba(31,198,216,.85), transparent 70%),
      radial-gradient(ellipse 700px 220px at 600px 470px, rgba(31,198,216,.75), transparent 70%),
      radial-gradient(ellipse 420px 420px at 250px 150px, rgba(90,79,208,.8), transparent 70%),
      radial-gradient(ellipse 380px 380px at 450px 260px, rgba(63,127,224,.7), transparent 70%),
      linear-gradient(180deg, var(--night) 0%, #0d2a4d 45%, #071a33 60%, var(--navy) 75%, #000 100%);
  }
  .top-strip {
    position: absolute; left: 0; top: 0; width: 1200px; height: 40px;
    background: linear-gradient(90deg, rgba(11,74,158,.2), var(--brand-blue-dark));
  }
  .brand-tab {
    position: absolute; right: 0; top: 0; width: 500px; height: 143px;
    background: var(--brand-blue);
    border-bottom-left-radius: 40px;
  }
  .brand-name {
    position: absolute; right: 60px; top: 70px;
    display: flex; align-items: center; gap: 12px;
    font-weight: 700; font-size: 40px; letter-spacing: -0.5px; color: var(--white);
  }
  .brand-dot { width: 16px; height: 16px; border-radius: 50%; background: var(--white); }
  .headline {
    position: absolute; left: 78px; top: 190px;
    font-weight: 500; line-height: 1; color: var(--white);
    display: flex; align-items: baseline;
  }
  .headline .initial { font-size: 312px; letter-spacing: -4px; }
  .headline .rest { font-size: 176px; letter-spacing: 2px; }
  .divider {
    position: absolute; left: 89px; top: 608px; width: 1020px; height: 3px;
    background: linear-gradient(90deg, var(--white) 0%, rgba(255,255,255,.85) 60%, rgba(255,255,255,0) 100%);
  }
  .features { position: absolute; left: 89px; top: 624px; }
  .feature { white-space: nowrap; font-size: 44px; line-height: 1; letter-spacing: 3px; }
  .feature + .feature { margin-top: 21px; }
  .feature strong { font-weight: 700; }
  .feature .hi { color: var(--accent-red); font-weight: 700; }
  .feature.price { font-size: 34px; letter-spacing: 3.5px; margin-top: 14px; }
  .bottom-curve { position: absolute; left: 0; top: 0; }
  .free-word {
    position: absolute; left: 87px; top: 914px;
    font-family: "Barlow Condensed", "Arial Narrow", sans-serif;
    font-weight: 700; font-size: 180px; line-height: 1; letter-spacing: -2px; color: var(--ink);
    transform: scaleX(.86); transform-origin: left top;
  }
  .free-list {
    position: absolute; left: 367px; top: 945px; list-style: none;
    font-family: "Barlow Semi Condensed", "Arial Narrow", sans-serif;
    font-weight: 500; font-size: 38px; line-height: 46px; letter-spacing: 2px; color: var(--muted-ink);
  }
  .free-list li { display: flex; align-items: center; gap: 17px; }
  .free-list li::before {
    content: ""; width: 14px; height: 14px; border-radius: 50%; background: var(--accent-red);
  }
  .free-month {
    position: absolute; left: 87px; top: 1097px; white-space: nowrap;
    font-family: "Barlow Semi Condensed", "Arial Narrow", sans-serif;
    font-weight: 600; font-size: 49px; line-height: 1; letter-spacing: 1.5px; color: var(--accent-red);
  }
  .speed-badge {
    position: absolute; left: 792px; top: 875px; width: 476px; height: 476px;
    border-radius: 50%; background: var(--accent-red);
  }
  .speed-label, .speed-value {
    position: absolute; left: 840px; width: 330px; text-align: center; line-height: 1;
    font-family: "Barlow Condensed", "Arial Narrow", sans-serif; font-weight: 700; color: var(--white);
  }
  .speed-label { top: 931px; font-size: 46px; letter-spacing: 1px; }
  .speed-value { top: 958px; font-size: 168px; letter-spacing: 3px; }
  .speed-unit { position: absolute; left: 905px; top: 1112px; }
</style>
</head>
<body>
<main class="ad">
  <div class="scene" role="img" aria-label="Alaskan night sky with northern lights over mountain silhouettes and a shooting star"></div>
  <div class="top-strip"></div>
  <div class="brand-tab"></div>
  <div class="brand-name"><span class="brand-dot"></span>Northreach Satellite</div>

  <h1 class="headline"><span class="initial">K</span><span class="rest">ORVO</span></h1>

  <div class="divider"></div>
  <div class="features">
    <p class="feature"><span class="hi">FIBER OPTIC</span> based connection, Not satellite</p>
    <p class="feature"><strong>EXTREME</strong> <span class="hi">LOW LATENCY</span>, consistent speeds</p>
    <p class="feature price">Packages start at only <span class="hi">$89.99</span> for speeds to 100mbps.</p>
  </div>

  <svg class="bottom-curve" width="1200" height="1200" viewBox="0 0 1200 1200">
    <path d="M0,872 Q420,828 900,930 L900,1200 L0,1200 Z" fill="var(--brand-blue)"/>
    <path d="M0,893 Q420,850 900,950 L900,1200 L0,1200 Z" fill="var(--white)"/>
  </svg>

  <div class="free-word">FREE</div>
  <ul class="free-list">
    <li>EQUIPMENT</li>
    <li>INSTALLATION</li>
    <li>WIFI ROUTER</li>
  </ul>
  <p class="free-month">FIRST MONTH OF SERVICE</p>

  <div class="speed-badge"></div>
  <div class="speed-label">SPEEDS TO</div>
  <div class="speed-value">500</div>
  <svg class="speed-unit" width="216" height="48" viewBox="0 0 216 48">
    <g fill="none" stroke="var(--white)" stroke-width="5">
      <path d="M4,7 L20,24 L4,41" opacity=".35"/>
      <path d="M22,7 L38,24 L22,41" opacity=".6"/>
      <path d="M40,7 L56,24 L40,41" opacity=".85"/>
    </g>
    <path d="M62,2 L192,2 L214,24 L192,46 L62,46 L80,24 Z" fill="var(--white)"/>
    <text x="140" y="38" text-anchor="middle" font-family="Barlow Condensed, Arial Narrow, sans-serif" font-weight="700" font-size="36" fill="var(--accent-red)">MBPS</text>
  </svg>
</main>
</body>
</html>
```